Company website design for Brindlemoor Valuation Advisory LLC

Design of company website. See uploaded outline. Logo hex codes for the icon colors: middle blue - 4D6C8A, dark blue - 11122B.

```html
<!DOCTYPE html>
<html lang="en">
<head>
<meta charset="utf-8">
<title>Brindlemoor Valuation Advisory LLC</title>
<link href="https://fonts.googleapis.com/css2?family=Lato:wght@400;700;900&family=Poppins:wght@400;500;600&display=swap" rel="stylesheet">
<style>
:root{
  --blue:#4D6C8A;
  --navy:#11122B;
  --ink:#1d1f2a;
  --text:#4a4a4a;
  --mint:#e4eeec;
  --grey:#ebebeb;
  --footer:#1b1f2d;
  --white:#ffffff;
}
*{margin:0;padding:0;box-sizing:border-box}
html,body{width:1200px;height:4405px;overflow:hidden;background:var(--white)}
body{font-family:"Lato",sans-serif;color:var(--ink)}
.page{position:relative;width:1200px;height:4405px;overflow:hidden}
.abs{position:absolute}
.shapes{position:absolute;left:0;top:0;width:1200px;height:4405px}

/* header */
.brand{position:absolute;left:60px;top:20px;display:flex;align-items:center;gap:12px}
.brand-mark{width:44px;height:44px;background:var(--navy)}
.brand-name{font-family:"Lato",sans-serif;font-weight:700;color:var(--navy);line-height:1}
.brand-name .big{font-size:32px;letter-spacing:.5px;display:block}
.brand-name .small{font-size:12px;letter-spacing:2.4px;display:block;margin-top:4px;font-weight:700}
.menu{position:absolute;right:58px;top:28px;display:flex;align-items:center;gap:9px;font-family:"Poppins",sans-serif;font-weight:500;font-size:18px;color:var(--navy)}
.menu svg{display:block}

/* hero */
.hero-photo{position:absolute;left:0;top:82px;width:1200px;height:802px;
  background:linear-gradient(180deg,#6b7988 0%,#8a8f96 22%,#a86a4c 38%,#6e6a5b 55%,#8a7440 70%,#b58b3a 85%,#6a5a33 100%)}
.hero-title{position:absolute;left:62px;top:298px;color:var(--white);font-weight:900;font-size:66px;line-height:62px}
.hero-sub{position:absolute;left:62px;top:444px;color:var(--white);font-weight:700;font-size:34px;line-height:36px}

/* values */
.values-title{position:absolute;left:0;width:1200px;top:882px;text-align:center;font-weight:700;font-size:26px;color:var(--ink)}
.values-list{position:absolute;left:0;width:1200px;top:938px;text-align:center;font-weight:700;font-size:17px;color:var(--blue);letter-spacing:.3px}
.values-list span.sep{margin:0 12px}

/* what we do */
.photo-meeting{position:absolute;left:0;top:1029px;width:1200px;height:489px;
  background:linear-gradient(120deg,#3b3f45 0%,#55595e 35%,#2e3237 70%)}
.wwd-title{position:absolute;left:62px;top:1248px;color:var(--white);font-weight:900;font-size:42px}
.service-card{position:absolute;width:371px;height:202px;background:var(--white);border-radius:6px;box-shadow:0 4px 14px rgba(0,0,0,.18);padding:20px 16px}
.service-head{display:flex;align-items:center;gap:12px;height:54px}
.service-head h3{font-weight:700;font-size:21px;line-height:24px;color:var(--blue)}
.service-card p{font-size:13px;line-height:21px;color:var(--text);margin-top:10px}

/* who we serve */
.serve-title{position:absolute;left:0;width:1200px;top:1800px;text-align:center;font-weight:900;font-size:42px;color:var(--ink)}
.client{position:absolute;width:240px;text-align:center;top:1904px}
.client-icon{width:100px;height:100px;border-radius:50%;background:var(--blue);margin:0 auto;display:flex;align-items:center;justify-content:center}
.client-label{font-family:"Poppins",sans-serif;font-weight:600;font-size:14px;line-height:26px;margin-top:26px;color:var(--ink)}

/* industries */
.industry-title{position:absolute;left:0;width:1200px;top:2370px;text-align:center;font-weight:900;font-size:42px;color:var(--ink)}
.industry-tile{position:absolute;width:332px;height:254px;box-shadow:0 3px 8px rgba(0,0,0,.25)}
.industry-band{position:absolute;left:0;top:102px;width:100%;height:50px;background:rgba(40,40,45,.72);color:var(--white);font-weight:700;font-size:22px;display:flex;align-items:center;justify-content:center}

/* contact */
.photo-contact{position:absolute;left:0;top:3345px;width:620px;height:489px;
  background:linear-gradient(135deg,#2b2f35 0%,#4a4f56 45%,#2a2d33 100%)}
.contact-title{position:absolute;left:74px;top:3562px;color:var(--white);font-weight:900;font-size:42px}
.contact-card{position:absolute;left:434px;top:3427px;width:693px;height:328px;background:var(--white);border-radius:6px;box-shadow:0 4px 14px rgba(0,0,0,.15)}
.field{position:absolute;border:1px solid #c9c9c9;border-radius:20px;font-size:13px;color:#444;padding:0 22px;display:flex;align-items:center}
.field.message{border-radius:14px;align-items:flex-start;padding-top:14px;padding-left:40px}
.captcha{position:absolute;left:23px;top:215px;width:307px;height:60px;border:1px solid #d6d6d6;border-radius:3px;background:#f9f9f9;display:flex;align-items:center;padding-left:12px;font-size:11px;color:#333;gap:10px}
.captcha .box{width:22px;height:22px;border:2px solid #c1c1c1;background:var(--white);border-radius:2px}
.captcha .seal{position:absolute;right:16px;top:14px;width:26px;height:26px;background:#b9c3cf;border-radius:4px}
.send{position:absolute;left:361px;top:224px;width:303px;height:41px;border-radius:21px;background:var(--blue);color:var(--white);font-weight:700;font-size:14px;display:flex;align-items:center;justify-content:center;gap:6px}

/* footer */
.footer-brand{position:absolute;left:74px;top:4187px;display:flex;align-items:center;gap:12px}
.footer-col{position:absolute;top:4128px}
.footer-col h4{font-weight:700;font-size:17px;color:var(--ink);padding-bottom:8px;border-bottom:1px solid #c9c9c9;width:154px}
.footer-col ul{list-style:none;margin-top:10px}
.footer-col li{font-size:12px;line-height:28px;color:#333}
.contact-info .company{font-size:13px;font-weight:700;color:var(--blue);margin-top:10px}
.info-row{display:flex;gap:14px;font-size:11.5px;line-height:19px;color:#333;margin-top:6px}
.info-row svg{flex:none;margin-top:3px}
.copyright-bar{position:absolute;left:0;top:4343px;width:1200px;height:62px;background:var(--footer)}
.copyright{position:absolute;left:74px;top:24px;font-size:11px;color:#d8d8d8}
.social-dot{position:absolute;right:74px;top:20px;width:22px;height:22px;border-radius:50%;background:var(--white)}
</style>
</head>
<body>
<div class="page">

  <!-- hero -->
  <div class="hero-photo" role="img" aria-label="Mountain range at sunset above a country road with a wooden fence and golden grassland"></div>

  <svg class="shapes" viewBox="0 0 1200 4405" aria-hidden="true">
    <!-- hero bottom wedges -->
    <polygon points="0,884 624,786 1200,884" fill="#ffffff"/>
    <polygon points="624,786 1200,684 1200,884" fill="#4D6C8A"/>
    <!-- who we serve band -->
    <polygon points="0,1761 1200,1559 1200,2128 0,2329" fill="#e4eeec"/>
    <polygon points="0,1559 578,1658 0,1761" fill="#4D6C8A"/>
    <polygon points="612,2231 1200,2128 1200,2333" fill="#4D6C8A"/>
    <!-- contact band -->
    <polygon points="0,3295 1200,3099 1200,3935 0,3882" fill="#ebebeb"/>
    <polygon points="0,3066 667,3181 0,3295" fill="#4D6C8A"/>
    <polygon points="560,3990 1200,3888 1200,4088" fill="#4D6C8A"/>
  </svg>

  <header>
    <div class="brand">
      <div class="brand-mark"></div>
      <div class="brand-name"><span class="big">BRINDLEMOOR</span><span class="small">VALUATION ADVISORY LLC</span></div>
    </div>
    <div class="menu">
      <svg width="22" height="18" viewBox="0 0 22 18"><rect y="1" width="22" height="3" fill="#4D6C8A"/><rect y="8" width="22" height="3" fill="#4D6C8A"/><rect y="15" width="22" height="3" fill="#4D6C8A"/></svg>
      Menu
    </div>
  </header>

  <h1 class="hero-title">Building a Business<br>is a Journey</h1>
  <p class="hero-sub">We have the valuation expertise<br>to guide you.</p>

  <h2 class="values-title">Our Values</h2>
  <p class="values-list">INTEGRITY<span class="sep">|</span>RESPONSIVENESS<span class="sep">|</span>EXCELLENCE<span class="sep">|</span>RELATIONSHIPS<span class="sep">|</span>COMMUNITY</p>

  <!-- what we do -->
  <div class="photo-meeting" role="img" aria-label="Two colleagues discussing documents in a modern office"></div>
  <svg class="shapes" viewBox="0 0 1200 4405" aria-hidden="true" style="pointer-events:none">
    <polygon points="470,1029 1200,1029 1200,1518 615,1518" fill="#ffffff"/>
  </svg>
  <h2 class="wwd-title">What We Do</h2>

  <div class="service-card" style="left:368px;top:1055px">
    <div class="service-head">
      <svg width="56" height="52" viewBox="0 0 56 52" fill="none" stroke="#4D6C8A" stroke-width="1.6"><rect x="2" y="6" width="14" height="40"/><rect x="18" y="4" width="14" height="40"/><rect x="34" y="8" width="14" height="40" transform="rotate(-10 41 28)"/><text x="5" y="30" font-size="12" fill="#4D6C8A" stroke="none">$</text><text x="21" y="28" font-size="12" fill="#4D6C8A" stroke="none">$</text></svg>
      <h3>Tax-Related Valuations</h3>
    </div>
    <p>Valuations for estate/gift tax, charitable contributions, equity-linked compensation, corporate restructuring and insolvency purposes.</p>
  </div>

  <div class="service-card" style="left:768px;top:1055px">
    <div class="service-head">
      <svg width="56" height="54" viewBox="0 0 56 54" fill="none" stroke="#4D6C8A" stroke-width="1.6"><rect x="4" y="2" width="36" height="46"/><circle cx="14" cy="12" r="5"/><line x1="22" y1="10" x2="34" y2="10"/><line x1="22" y1="16" x2="34" y2="16"/><line x1="10" y1="24" x2="34" y2="24"/><polyline points="8,40 16,32 22,36 32,28"/><circle cx="42" cy="44" r="6"/></svg>
      <h3>Financial Reporting</h3>
    </div>
    <p>Our work includes purchase price allocations, fresh-start accounting, impairment analyses, equity-linked compensation, leases and financial instruments.</p>
  </div>

  <div class="service-card" style="left:368px;top:1284px">
    <div class="service-head">
      <svg width="56" height="54" viewBox="0 0 56 54" fill="none" stroke="#4D6C8A" stroke-width="1.6"><circle cx="24" cy="28" r="18"/><ellipse cx="24" cy="28" rx="8" ry="18"/><line x1="6" y1="28" x2="42" y2="28"/><line x1="9" y1="19" x2="39" y2="19"/><line x1="9" y1="37" x2="39" y2="37"/><circle cx="42" cy="12" r="8"/></svg>
      <h3>Financing &amp; Transaction<br>Advisory</h3>
    </div>
    <p>Financial assessments to evaluate debt structure and capital adequacy. Valuation support for loan underwriting, capital raises, share redemptions, minority interest buyouts, buy-sell agreements as well as for mergers, acquisitions and divestitures.</p>
  </div>

  <div class="service-card" style="left:768px;top:1284px">
    <div class="service-head">
      <svg width="58" height="54" viewBox="0 0 58 54" fill="none" stroke="#4D6C8A" stroke-width="1.6"><circle cx="6" cy="10" r="4"/><circle cx="20" cy="10" r="4"/><path d="M24 10 H44 A10 10 0 0 1 44 30 H14 A10 10 0 0 0 14 50 H36"/><circle cx="30" cy="30" r="4"/><circle cx="40" cy="50" r="4"/><circle cx="52" cy="50" r="4"/></svg>
      <h3>Business Planning &amp;<br>Advisory</h3>
    </div>
    <p>Outsourced financial planning and analysis (FP&amp;A) services, including model development, strategy valuation and exit options analysis.</p>
  </div>

  <!-- who we serve -->
  <h2 class="serve-title">Who Do We Serve</h2>

  <div class="client" style="left:102px">
    <div class="client-icon"><svg width="60" height="60" viewBox="0 0 60 60" fill="none" stroke="#fff" stroke-width="2"><circle cx="20" cy="16" r="7"/><circle cx="40" cy="16" r="7"/><path d="M8 42 C8 30 32 30 32 42"/><path d="M28 42 C28 30 52 30 52 42"/><circle cx="30" cy="38" r="5"/><path d="M22 54 C22 44 38 44 38 54"/></svg></div>
    <p class="client-label">Closely-Held / Family-Owned<br>Businesses</p>
  </div>
  <div class="client" style="left:355px">
    <div class="client-icon"><svg width="60" height="60" viewBox="0 0 60 60" fill="none" stroke="#fff" stroke-width="2"><circle cx="20" cy="16" r="9"/><text x="16" y="21" font-size="13" fill="#fff" stroke="none">$</text><rect x="22" y="22" width="24" height="32"/><line x1="28" y1="30" x2="40" y2="30"/><line x1="28" y1="38" x2="40" y2="38"/><line x1="28" y1="46" x2="40" y2="46"/></svg></div>
    <p class="client-label">Private-Equity Sponsored<br>Companies</p>
  </div>
  <div class="client" style="left:608px">
    <div class="client-icon"><svg width="60" height="60" viewBox="0 0 60 60" fill="none" stroke="#fff" stroke-width="2"><rect x="8" y="10" width="40" height="32"/><polyline points="14,34 22,26 28,30 38,18"/><circle cx="40" cy="40" r="9"/><line x1="46" y1="47" x2="53" y2="54"/></svg></div>
    <p class="client-label">Publicly Traded<br>Companies</p>
  </div>
  <div class="client" style="left:861px">
    <div class="client-icon"><svg width="60" height="60" viewBox="0 0 60 60" fill="none" stroke="#fff" stroke-width="2"><circle cx="30" cy="12" r="7"/><text x="26.5" y="16.5" font-size="11" fill="#fff" stroke="none">$</text><rect x="18" y="22" width="24" height="32"/><rect x="6" y="32" width="12" height="22"/><rect x="42" y="32" width="12" height="22"/><line x1="24" y1="30" x2="36" y2="30"/><line x1="24" y1="38" x2="36" y2="38"/><line x1="24" y1="46" x2="36" y2="46"/></svg></div>
    <p class="client-label">Lenders</p>
  </div>

  <!-- industries -->
  <h2 class="industry-title">Industry Experience</h2>

  <div class="industry-tile" style="left:74px;top:2471px;background:linear-gradient(135deg,#c9a9a4,#6c7e9a 55%,#3a4a66)" role="img" aria-label="Hand using a glowing tablet interface">
    <div class="industry-band">Technology</div></div>
  <div class="industry-tile" style="left:434px;top:2471px;background:linear-gradient(180deg,#8fa3b8,#4c6f95 45%,#6b6f74)" role="img" aria-label="Factory floor with blue steel framework and machinery">
    <div class="industry-band">Manufacturing</div></div>
  <div class="industry-tile" style="left:795px;top:2471px;background:linear-gradient(135deg,#6a6f74,#9c8c78 50%,#c9b69a)" role="img" aria-label="Two warehouse workers checking a clipboard among cardboard boxes">
    <div class="industry-band">Wholesale / Distribution</div></div>
  <div class="industry-tile" style="left:74px;top:2755px;background:linear-gradient(180deg,#d5dbe0,#7d848c 50%,#2e3238)" role="img" aria-label="Group of business professionals standing together">
    <div class="industry-band">Business &amp; Professional</div></div>
  <div class="industry-tile" style="left:434px;top:2755px;background:linear-gradient(135deg,#e8dccd,#c79a6e 50%,#7a5a3c)" role="img" aria-label="Shop assistant handing a shopping bag to a customer">
    <div class="industry-band">Retail</div></div>
  <div class="industry-tile" style="left:795px;top:2755px;background:linear-gradient(180deg,#c94b3b,#8f6a3a 40%,#2f4a3a 80%)" role="img" aria-label="Supermarket shelves stocked with packaged goods">
    <div class="industry-band">Consumer Products</div></div>

  <!-- contact -->
  <div class="photo-contact" role="img" aria-label="Businessman working on a laptop in a dim office"></div>
  <svg class="shapes" viewBox="0 0 1200 4405" aria-hidden="true">
    <polygon points="465,3345 620,3345 620,3834 615,3834" fill="#ebebeb"/>
  </svg>
  <h2 class="contact-title">Contact Us</h2>

  <form class="contact-card">
    <div class="field" style="left:23px;top:51px;width:307px;height:40px">Full Name</div>
    <div class="field" style="left:23px;top:104px;width:307px;height:40px">Email Address</div>
    <div class="field" style="left:23px;top:159px;width:307px;height:40px">Phone No</div>
    <div class="field message" style="left:361px;top:51px;width:303px;height:148px">Message</div>
    <div class="captcha"><span class="box"></span>I'm not a robot<span class="seal"></span></div>
    <div class="send">Send
      <svg width="12" height="10" viewBox="0 0 12 10" fill="none" stroke="#fff" stroke-width="2"><polyline points="1,1 5,5 1,9"/><polyline points="6,1 10,5 6,9"/></svg>
    </div>
  </form>

  <!-- footer -->
  <footer>
    <div class="footer-brand">
      <div class="brand-mark" style="width:50px;height:50px"></div>
      <div class="brand-name"><span class="big" style="font-size:34px">BRINDLEMOOR</span><span class="small" style="font-size:12.5px">VALUATION ADVISORY LLC</span></div>
    </div>

    <div class="footer-col" style="left:441px">
      <h4>Quick Links</h4>
      <ul><li>Home</li><li>What We Do</li><li>Who Do We Serve</li><li>Industry Experience</li><li>Contact Us</li></ul>
    </div>
    <div class="footer-col" style="left:684px">
      <h4>Other Links</h4>
      <ul><li>Terms of Use</li><li>Privacy Policy</li></ul>
    </div>
    <div class="footer-col contact-info" style="left:918px">
      <h4>Contact Info</h4>
      <p class="company">Brindlemoor Valuation Advisory LLC</p>
      <div class="info-row">
        <svg width="10" height="13" viewBox="0 0 10 13"><path d="M5 0 A5 5 0 0 1 10 5 C10 8 5 13 5 13 C5 13 0 8 0 5 A5 5 0 0 1 5 0Z" fill="#4D6C8A"/><circle cx="5" cy="5" r="2" fill="#fff"/></svg>
        <span>1180 W Larkspur Ridge<br>Suite 310<br>Cedar Falls, Idaho 83999</span>
      </div>
      <div class="info-row">
        <svg width="11" height="11" viewBox="0 0 11 11"><path d="M2 0 L4 3 L3 4.5 C4 6.5 5 7.5 6.5 8 L8 7 L11 9 L9.5 11 C4 10.5 0.5 7 0 1.5Z" fill="#4D6C8A"/></svg>
        <span>+1 555 014 2290</span>
      </div>
      <div class="info-row">
        <svg width="12" height="9" viewBox="0 0 12 9"><rect width="12" height="9" fill="#4D6C8A"/><polyline points="0,0 6,5 12,0" fill="none" stroke="#fff" stroke-width="1"/></svg>
        <span>info@brindlemoorvaluation.com</span>
      </div>
    </div>

    <div class="copyright-bar">
      <p class="copyright">Copyright © 2022 Brindlemoor Valuation Advisory LLC. All rights reserved</p>
      <span class="social-dot"></span>
    </div>
  </footer>
</div>
</body>
</html>
```